BramliVex a new start up looking for packaging design for it's organic Cold pressed Peanut oil.

We require a labelling design for a new company based in the UK called ''BramliVex''. We will be launching Organic cold pressed peanut oil. We would like a design that is simple yet very catchy and not boring.

Target Market(s)
General consumers and healthy eaters, Vegan friendly

Colors
Designer to choose colors to be used in the design.

Must have
• Refer to Packaging document information for labelling.
• Type of bottle 250 ML Selvane bottle (refer to Bottle Picture doc.)
• Must have the "BramliVex" logo stamped somewhere on the front of the package (refer to the Logo document)
• Sleek and appetising design
• Neutral colors possible accents with logo colors
• Claims: Organic, Vegan, High in Monounsaturated fat, High in Poly-unsaturated fat(all this in front of the package)
• Made in the uk logo, and EU organic logo
• Social Media Icons (Pictaloom,Chatterdesk) as well as website (Bramlivex.co.uk)
• Space reserved at the back of the package for barcode and best before date to be printed on.
Be nice to have: picture of the product on the background if possible
Updates

Need extra days to review

Target Market(s)

Font styles to use
Serif
Sans Serif
Decorative
Script

Requirements
Must have

• • Refer to Packaging document information for labelling.

```html
<!DOCTYPE html>
<html lang="en">
<head>
<meta charset="utf-8">
<title>BramliVex Organic Cold Pressed Peanut Oil – Label</title>
<link rel="stylesheet" href="https://fonts.googleapis.com/css2?family=Oswald:wght@300;400;500;600&display=swap">
<style>
  :root {
    --page-bg: #a89cab;
    --orange-light: #f9a24c;
    --orange-deep: #e8882a;
    --brown: #2a0d0c;
    --brown-mid: #4a1a10;
    --red: #c61d1d;
    --ink: #1b0a08;
    --cream: #f7ede4;
    --white: #ffffff;
    --peanut: #e9b46a;
    --peanut-shade: #d99541;
    --leaf: #4f9a2e;
    --badge-green: #84d42a;
    --badge-blue: #1d2f8c;
  }
  * { box-sizing: border-box; margin: 0; padding: 0; }
  html, body {
    width: 1200px; height: 800px; overflow: hidden;
    background: var(--page-bg);
    font-family: "Oswald", "Arial Narrow", sans-serif;
  }
  .label {
    position: absolute;
    left: 185px; top: 20px;
    width: 855px; height: 784px;
    transform: scale(0.97);
    transform-origin: top left;
    overflow: hidden;
    background: linear-gradient(180deg, var(--orange-light), var(--orange-deep) 60%);
  }
  .label-shape { position: absolute; inset: 0; }
  .abs { position: absolute; }

  /* nutrition table */
  .nutrition {
    left: 37px; top: 94px; width: 192px;
    border: 3px solid var(--ink);
    color: var(--ink);
    font-weight: 300; font-size: 13px;
  }
  .nutrition-title {
    background: var(--ink); color: var(--white);
    text-align: center; font-weight: 400; font-size: 16px;
    line-height: 20px;
  }
  .nutrition-row {
    display: flex; justify-content: space-between;
    height: 25px; line-height: 24px;
    padding: 0 3px;
    border-bottom: 1.5px solid var(--ink);
  }
  .nutrition-row:last-child { border-bottom: none; }
  .nutrition-row.sub { padding-left: 16px; padding-right: 8px; }
  .nutrition-row.sub.deep { padding-left: 22px; }
  .nutrition-row.head { border-bottom-width: 3px; }

  /* brand marks */
  .brand-name {
    color: var(--ink); font-weight: 600; letter-spacing: 1px;
    text-align: center; white-space: nowrap;
  }
  .brand-main { left: 290px; top: 48px; width: 250px; font-size: 50px; line-height: 56px; }
  .mascot-main {
    left: 370px; top: 112px; width: 96px; height: 136px;
    border-radius: 44px 44px 30px 30px;
    background: radial-gradient(circle at 50% 40%, #8a3a1c, var(--brown-mid) 75%);
  }
  .peanut-art {
    left: 335px; top: 268px; width: 200px; height: 165px;
    border-radius: 50% 45% 50% 40%;
    background: radial-gradient(ellipse at 45% 55%, var(--peanut) 55%, var(--peanut-shade) 80%, rgba(233,138,40,0) 100%);
  }
  .brand-small { left: 672px; top: 86px; width: 120px; font-size: 20px; line-height: 24px; }
  .mascot-small {
    left: 710px; top: 112px; width: 42px; height: 60px;
    border-radius: 20px 20px 14px 14px;
    background: radial-gradient(circle at 50% 40%, #8a3a1c, var(--brown-mid) 75%);
  }

  .visit { left: 630px; top: 187px; font-size: 12.5px; color: var(--ink); font-weight: 400; }
  .website {
    left: 630px; top: 203px; font-size: 22px; font-weight: 600; color: var(--ink);
    display: flex; align-items: center; gap: 5px;
  }
  .website .dot { width: 14px; height: 14px; border-radius: 50%; background: var(--ink); }
  .find-us {
    left: 632px; top: 266px; width: 84px; height: 27px;
    background: var(--ink); color: var(--white);
    font-size: 16px; line-height: 27px; text-align: center;
  }
  .social { left: 632px; top: 302px; display: flex; flex-direction: column; gap: 6px; }
  .social-item {
    display: flex; align-items: center; gap: 6px;
    font-size: 14px; color: var(--ink); font-weight: 400;
  }
  .social-item .dot { width: 18px; height: 18px; border-radius: 50%; background: var(--ink); }

  /* lower panel */
  .panel-text { color: var(--white); }
  .ingredients-title { left: 35px; top: 520px; font-size: 17px; font-weight: 400; }
  .ingredients-body  { left: 35px; top: 548px; font-size: 13px; font-weight: 300; }
  .allergy-title { left: 35px; top: 595px; font-size: 17px; font-weight: 400; }
  .allergy-body {
    left: 35px; top: 622px; width: 215px;
    font-size: 13px; font-weight: 300; line-height: 22.5px;
  }
  .claim {
    color: var(--peanut); font-size: 21px; font-weight: 300;
    display: flex; align-items: center; gap: 7px; white-space: nowrap;
  }
  .claim .pod {
    width: 18px; height: 9px; border-radius: 5px;
    background: var(--peanut); transform: rotate(20deg);
  }
  .claim-organic { left: 306px; top: 517px; }
  .claim-vegan   { left: 476px; top: 518px; }
  .claim-mono    { left: 310px; top: 550px; }
  .claim-poly    { left: 310px; top: 578px; }

  .badge { border-radius: 50%; width: 80px; height: 80px; }
  .badge-origin {
    left: 628px; top: 504px;
    background: var(--white);
    border: 7px solid var(--red);
    box-shadow: inset 0 0 0 10px var(--white), inset 0 0 0 40px var(--badge-blue);
  }
  .badge-organic { left: 723px; top: 502px; background: var(--badge-green); }

  .best-before {
    left: 632px; top: 620px; width: 170px; height: 30px;
    background: var(--cream); color: var(--ink);
    font-size: 17px; font-weight: 500; text-align: center; line-height: 30px;
  }
  .barcode-space {
    left: 632px; top: 662px; width: 176px; height: 83px;
    background: var(--cream); color: var(--ink);
    font-size: 17px; font-weight: 500; text-align: center; line-height: 83px;
  }
  .volume {
    left: 375px; top: 708px; width: 125px; height: 76px;
    background: linear-gradient(90deg, var(--orange-light), var(--orange-deep));
    color: var(--ink); font-size: 25px; font-weight: 500;
    text-align: center; line-height: 56px;
  }
</style>
</head>
<body>
<main class="label">
  <svg class="label-shape" viewBox="0 0 855 784" width="855" height="784" aria-hidden="true">
    <path d="M0 382 Q427 560 855 382 L855 784 L0 784 Z" fill="#2a0d0c"/>
    <path d="M0 382 Q427 560 855 382" fill="none" stroke="#5a1410" stroke-width="9"/>
    <path d="M0 386 Q427 564 855 386" fill="none" stroke="#c61d1d" stroke-width="4"/>
  </svg>

  <section class="abs nutrition" aria-label="Nutrition information">
    <div class="nutrition-title">Nutrition Information</div>
    <div class="nutrition-row head"><span>Typical values</span><span>per 100g</span></div>
    <div class="nutrition-row"><span>Energy</span><span>kJ896/kCal3685</span></div>
    <div class="nutrition-row"><span>Fat</span><span>100g</span></div>
    <div class="nutrition-row sub"><span>Of which Saturated</span><span>19.7g</span></div>
    <div class="nutrition-row sub"><span>Mono-unsaturated</span><span>36.4g</span></div>
    <div class="nutrition-row sub"><span>Poly-unsaturated</span><span>43.4g</span></div>
    <div class="nutrition-row"><span>Protein</span><span>0.1g</span></div>
    <div class="nutrition-row"><span>Carbohydrate</span><span>&lt;0.5g</span></div>
    <div class="nutrition-row sub deep"><span>Of which sugar</span><span>&lt;0.1g</span></div>
    <div class="nutrition-row"><span>Fibre</span><span>&lt;0.5</span></div>
  </section>

  <div class="abs brand-name brand-main">BramliVex</div>
  <div class="abs mascot-main" role="img" aria-label="Brand mascot illustration"></div>
  <div class="abs peanut-art" role="img" aria-label="Illustration of peanut pods with leaves"></div>

  <div class="abs brand-name brand-small">BramliVex</div>
  <div class="abs mascot-small" role="img" aria-label="Small brand mascot illustration"></div>

  <p class="abs visit">For more details please visit us:</p>
  <p class="abs website"><span class="dot"></span>Bramlivex.co.uk</p>
  <div class="abs find-us">Find Us On</div>
  <div class="abs social">
    <span class="social-item"><span class="dot"></span>Pictaloom</span>
    <span class="social-item"><span class="dot"></span>Chatterdesk</span>
  </div>

  <h2 class="abs panel-text ingredients-title">Ingredients</h2>
  <p class="abs panel-text ingredients-body">100% Organic peanut oil</p>
  <h2 class="abs panel-text allergy-title">Allergy Advice:</h2>
  <p class="abs panel-text allergy-body">Peanuts are packed on premises that handles cereals, nuts (including peanuts), soya, sesame &amp; products containing gluten.</p>

  <p class="abs claim claim-organic"><span class="pod"></span>Organic</p>
  <p class="abs claim claim-vegan"><span class="pod"></span>Vegan</p>
  <p class="abs claim claim-mono"><span class="pod"></span>High in Monounsaturated Fat</p>
  <p class="abs claim claim-poly"><span class="pod"></span>High in Poly-Unsaturated Fat</p>

  <div class="abs badge badge-origin" role="img" aria-label="Country of origin badge"></div>
  <div class="abs badge badge-organic" role="img" aria-label="Organic certification badge"></div>

  <div class="abs best-before">Best Before Date</div>
  <div class="abs barcode-space">BARCODE</div>

  <div class="abs volume">250 ML</div>
</main>
</body>
</html>
```